Pine Ridge Traders, LLC- Global Beverage Company with 100% Cold Chain Logistics

Hey All, My Name is Dale, I am a young business owner in a competitive export space, but my niche is that I am shipping all of my beer around the world, "100% Cold Chain". This model is more costly, but it protects the integrity of the beer itself and will give folks in foreign countries the best representation of what US Craft Beer has to offer.

I am not a branding guy and don't claim to be one, I am a salesperson first, and will be referring to all of you to create something great that will be memorable.

I am looking for a basic Business Card Design for my Craft Beer Export company. I sell US Craft Beer in several countries around the globe. Austrailia, China, Taiwan, Chile, France, New Zealand... to name a few.

I am looking for a sleek, modern, and fresh design. Quickly!

Thanks for your consideration!

Cheers,

Dale

Target Market(s)

International

Contact Information for Business Card

Dale Corwin
Founder- Roving Hops Guy
Dale@PineRidgeTraders.example
@RovingHopsGuy- Instagram only
www.Pineridgetraders.example
@PineRidgeTradersAU- Instagram Only

Font styles to use
Serif

Colors
0592cd
ffffff

Requirements
Must have
• Name-
• Title-
• Email-
• Social Media Handle-
• Company Website-
Nice to have
• Nice Logo/ Images on Card
Should not have
• Tacky Beer Images

```html
<!DOCTYPE html>
<html lang="en">
<head>
<meta charset="utf-8">
<title>Dale Corwin — Business Card</title>
<link rel="stylesheet" href="https://fonts.googleapis.com/css2?family=Tinos:wght@400;700&display=swap">
<style>
  :root {
    --canvas: #e9e9ec;
    --card: #000000;
    --shade-1: #1d1d1f;
    --shade-2: #121213;
    --gold: #e9b023;
    --gold-deep: #8a6410;
    --white: #ffffff;
  }
  * { margin: 0; padding: 0; box-sizing: border-box; }
  html, body {
    width: 1200px; height: 1176px; overflow: hidden;
    background: var(--canvas);
    font-family: "Tinos", "Times New Roman", serif;
  }
  .sheet {
    position: relative; width: 1200px; height: 1176px;
    display: flex; flex-direction: column; align-items: center;
    justify-content: space-evenly;
  }
  .card {
    position: relative; width: 900px; height: 548px;
    background: var(--card); overflow: hidden;
    box-shadow: 0 6px 18px rgba(0,0,0,.25);
  }
  .card__art { position: absolute; inset: 0; width: 100%; height: 100%; }
  .card__name {
    position: absolute; right: 24px; top: 54px;
    color: var(--white); font-weight: 700; font-size: 80px; line-height: 1;
    letter-spacing: .5px;
  }
  .card--back .card__name { right: 76px; top: 62px; font-size: 68px; }
  .card__title {
    position: absolute; right: 112px; top: 134px;
    color: var(--gold); font-size: 32px; line-height: 1;
  }
  .contacts {
    position: absolute; left: 84px; top: 312px; list-style: none;
  }
  .contacts__item {
    display: flex; align-items: center; height: 50px; margin-bottom: 18px;
    color: var(--white); font-size: 30px;
  }
  .contacts__icon { width: 48px; height: 48px; margin-right: 24px; flex: none; }
</style>
</head>
<body>
<main class="sheet">

  <section class="card card--front" aria-label="Card front">
    <svg class="card__art" viewBox="0 0 900 548" aria-hidden="true">
      <defs>
        <linearGradient id="front-shade" x1="0" y1="0" x2="1" y2="1">
          <stop offset="0" stop-color="#2a2a2c"/>
          <stop offset="1" stop-color="#050505"/>
        </linearGradient>
        <linearGradient id="front-gold" x1="0" y1="0" x2="1" y2="0">
          <stop offset="0" stop-color="var(--gold)" stop-opacity="0"/>
          <stop offset=".55" stop-color="var(--gold-deep)"/>
          <stop offset="1" stop-color="var(--gold)"/>
        </linearGradient>
      </defs>
      <polygon points="0,0 210,0 590,548 0,548" fill="url(#front-shade)"/>
      <polygon points="0,0 60,0 440,548 0,548" fill="#0e0e0f" opacity=".7"/>
      <rect x="570" y="526" width="330" height="22" fill="url(#front-gold)"/>
    </svg>
    <h1 class="card__name">Dale Corwin</h1>
  </section>

  <section class="card card--back" aria-label="Card back">
    <svg class="card__art" viewBox="0 0 900 548" aria-hidden="true">
      <defs>
        <linearGradient id="back-shade" x1="0" y1="0" x2="1" y2="1">
          <stop offset="0" stop-color="#2a2a2c"/>
          <stop offset="1" stop-color="#060606"/>
        </linearGradient>
        <linearGradient id="gold-right" x1="0" y1="0" x2="1" y2="0">
          <stop offset="0" stop-color="var(--gold)" stop-opacity="0"/>
          <stop offset=".4" stop-color="var(--gold-deep)"/>
          <stop offset="1" stop-color="var(--gold)"/>
        </linearGradient>
        <linearGradient id="gold-left" x1="0" y1="0" x2="1" y2="0">
          <stop offset="0" stop-color="var(--gold)"/>
          <stop offset=".6" stop-color="var(--gold-deep)"/>
          <stop offset="1" stop-color="var(--gold-deep)" stop-opacity="0"/>
        </linearGradient>
      </defs>
      <polygon points="0,0 210,0 400,232 0,232" fill="url(#back-shade)"/>
      <polygon points="0,0 80,0 270,232 0,232" fill="#0e0e0f" opacity=".7"/>
      <rect x="380" y="228" width="520" height="27" fill="url(#gold-right)"/>
      <rect x="0" y="255" width="520" height="27" fill="url(#gold-left)"/>
    </svg>

    <h1 class="card__name">Dale Corwin</h1>
    <p class="card__title">Founder- Roving Hops Guy</p>

    <ul class="contacts">
      <li class="contacts__item">
        <svg class="contacts__icon" viewBox="0 0 48 48" aria-hidden="true">
          <circle cx="24" cy="24" r="21" fill="none" stroke="var(--gold)" stroke-width="2.5"/>
          <rect x="13" y="16" width="22" height="16" rx="2" fill="var(--gold)"/>
          <path d="M14 18 L24 26 L34 18" fill="none" stroke="#000" stroke-width="2"/>
        </svg>
        <span>Dale@PineRidgeTraders.example</span>
      </li>
      <li class="contacts__item">
        <svg class="contacts__icon" viewBox="0 0 48 48" aria-hidden="true">
          <circle cx="24" cy="24" r="21" fill="none" stroke="var(--gold)" stroke-width="2.5"/>
        </svg>
        <span>@RovingHopsGuy</span>
      </li>
      <li class="contacts__item">
        <svg class="contacts__icon" viewBox="0 0 48 48" aria-hidden="true">
          <circle cx="24" cy="24" r="21" fill="none" stroke="var(--gold)" stroke-width="2.5"/>
          <g fill="none" stroke="var(--gold)" stroke-width="1.8">
            <circle cx="24" cy="24" r="13"/>
            <ellipse cx="24" cy="24" rx="6" ry="13"/>
            <line x1="11" y1="24" x2="37" y2="24"/>
            <line x1="24" y1="11" x2="24" y2="37"/>
            <path d="M13 17 H35 M13 31 H35"/>
          </g>
        </svg>
        <span>www.Pineridgetraders.example</span>
      </li>
    </ul>
  </section>

</main>
</body>
</html>
```